Need Help Rebranding My Food Blog

I have a Wordpress Food blog called BeetBuddies.com. Right now it has no life and is very bland. I am rebranding this site to a new named called, TheHoneyedDays.com. I would love to have a blog that is vibrant and full of life and personality.

One of my top priorities when a new visitor comes to my site is to quickly understand what the site is about (Gluten-free, dairy-free sweets that taste delicious).

I also want people to feel a connection with me when they come to the site.

Here are some other things that I'd like in the blog design...

1. Optin
My business is driven by adding people to my list so it is very important for me to have an optin front and center/ above-the-fold. See https://www.quietrevenuehub.com/ as an example. The headline that I would like is "Gluten-free & dairy-free sweets that actually taste good"

2. Vibrant/full life
The next important aspect of this blog is that it is vibrant. I like colors that remind me of a SUNSET. See attachments for logo and color scheme. Here's an example of a site I really like that is vibrant: http://www.mellowplateliving.com/

Also see Image titled: "Sample: Feeling". Notice the feeling you get from the image/brush strokes and how it feels light, breezy, and free spirited.

3. Food Images
The last important aspect for my blog is to showcase my recipes. I have attached a few of them as examples. Its really important for a food blog to showcase beautiful pictures of recipes for people to see so will definitely need this in the design.

Also, attached...
1. Image of me.
2. New logo for TheHoneyedDays (notice: don't use the one attached as "Sample/Feeling". That's just for reference of the feeling I like.)

Thanks!

Rosalind

P.S. I didn't include all the copy that would be needed so feel free to use the "lorem ipsum" text as placeholder if need be.

Target Market(s)

stay-at-home moms, dairy-free & gluten allergies, love desserts & sweets

Coding

Coded - Design and coding required

Font styles to use
Sans Serif

Requirements
Must have
• 1. Optin area with my picture and what I'm about ""Gluten-free & dairy-free sweets that actually taste good""
• 2. Must have personality/vibrancy to the site. Think full of life, not dull like my current website... beetbuddies.com
• 3. Highlight food images (Vertical image holders only)
Nice to have
• Color scheme should be based on my logo
Should not have
• No black or grey colors

```html
<!DOCTYPE html>
<html lang="en">
<head>
<meta charset="utf-8">
<title>The Honeyed Days</title>
<link href="https://fonts.googleapis.com/css2?family=Dancing+Script:wght@500;700&family=Montserrat:wght@400;500;600&display=swap" rel="stylesheet">
<style>
:root{
  --orange:#f08a4b;
  --orange-soft:#f6a772;
  --peach:#f9c3a0;
  --pink:#e2456f;
  --pink-deep:#d8336a;
  --rose:#ee8fa6;
  --paper:#f3f1f0;
  --white:#ffffff;
  --ink:#6a4a52;
  --script:"Dancing Script", cursive;
  --sans:"Montserrat", sans-serif;
}
*{box-sizing:border-box;margin:0;padding:0}
html,body{width:1200px;height:3482px;overflow:hidden}
body{position:relative;font-family:var(--sans);color:var(--ink);background:var(--paper)}
.abs{position:absolute}
.wave{position:absolute;left:0;width:1200px;height:22px;display:block}
.btn{position:absolute;display:flex;align-items:center;justify-content:center;gap:8px;border-radius:26px;font:600 17px var(--sans);letter-spacing:.5px;text-transform:uppercase}
.btn-light{background:var(--white);color:var(--pink)}
.btn-pink{background:var(--pink);color:var(--white)}

/* header */
.site-header{position:absolute;top:0;left:0;width:1200px;height:70px;background:var(--white);z-index:3}
.main-nav{position:absolute;left:79px;top:20px;display:flex;gap:14px;font:500 19px var(--script);color:var(--pink)}
.main-nav .current{text-decoration:underline}
.brand{position:absolute;left:418px;top:14px;width:370px;height:120px;display:flex;align-items:center;justify-content:center;gap:12px;background:var(--white);border-radius:0 0 60px 60px;z-index:4}
.brand-name{font:700 46px var(--script);color:var(--pink)}
.brand-dot{width:16px;height:16px;border-radius:50%;background:var(--orange)}
.search{position:absolute;left:853px;top:14px;width:266px;height:38px;border:2px solid #f0d3da;border-radius:20px;background:var(--white);font:italic 14px var(--sans);color:#b9a2a8;padding:9px 18px}
.search-btn{position:absolute;right:4px;top:4px;width:26px;height:26px;border-radius:50%;background:var(--pink)}

/* hero */
.hero{position:absolute;top:0;left:0;width:1200px;height:673px;background:linear-gradient(90deg,var(--orange) 0%,#ec6a5d 45%,var(--pink) 100%)}
.hero-photo{position:absolute;left:0;top:104px;width:560px;height:569px;background:linear-gradient(160deg,#f4b08a,#e08a6e 60%,#d87a68);border-radius:0 240px 0 0}
.cake-plate{position:absolute;left:905px;top:62px;width:295px;height:286px;background:radial-gradient(circle at 58% 45%,#7a4a3a 0 42%,#f3efee 43% 100%);border-radius:150px 0 0 150px}
.hero-tagline{position:absolute;left:383px;top:296px;width:560px;font:500 54px/64px var(--script);color:var(--white)}
.hero-sign{position:absolute;left:522px;top:522px;font:500 54px var(--script);color:var(--white)}
.hero-arrow{position:absolute;left:460px;top:470px}

/* newsletter */
.newsletter{position:absolute;top:673px;left:0;width:1200px;height:290px;background:var(--paper);text-align:center}
.newsletter h2{position:absolute;top:48px;width:100%;font:500 42px var(--script);color:var(--pink)}
.newsletter p{position:absolute;top:110px;left:290px;width:620px;font:15px/23px var(--sans);color:var(--ink)}
.nl-input{position:absolute;left:314px;top:183px;width:414px;height:52px;border:2px solid #e3dadb;border-radius:26px;background:var(--white);font:italic 15px var(--sans);color:#a99;text-align:left;padding:15px 30px}

/* welcome */
.welcome{position:absolute;top:963px;left:0;width:1200px;height:372px;background:linear-gradient(180deg,var(--orange) 0%,var(--orange-soft) 55%,var(--peach) 100%)}
.welcome h2{position:absolute;left:79px;top:44px;font:500 44px var(--script);color:var(--white)}
.welcome p{position:absolute;left:79px;top:112px;width:600px;font:14px/26px var(--sans);color:var(--white)}
.icecream{position:absolute;left:668px;top:35px;width:446px;height:279px;background:radial-gradient(ellipse at 55% 40%,#f1c468 0 35%,#e9b35a 36%,rgba(249,220,200,.7) 60%,rgba(255,255,255,0) 72%);border-radius:50%}

/* family */
.family-photo{position:absolute;top:1335px;left:0;width:1200px;height:626px;background:linear-gradient(180deg,#4a3a2e 0%,#8a7a62 40%,#b0a07c 70%,#6e6250 100%)}

/* about */
.about{position:absolute;top:1961px;left:0;width:1200px;height:337px;background:linear-gradient(180deg,var(--pink) 0%,#ea6f8f 60%,var(--rose) 100%);text-align:center}
.about h2{position:absolute;top:44px;width:100%;font:500 42px var(--script);color:var(--white)}
.about p{position:absolute;left:150px;top:118px;width:900px;font:14px/26px var(--sans);color:var(--white)}

/* recipes */
.recipes{position:absolute;top:2298px;left:0;width:1200px;height:592px;background:var(--paper)}
.recipes h2{position:absolute;top:18px;width:100%;text-align:center;font:500 42px var(--script);color:var(--pink)}
.recipe-card{position:absolute;top:109px;width:234px;height:327px;background:var(--white)}
.recipe-img{width:234px;height:269px}
.recipe-card h3{height:58px;display:flex;align-items:center;justify-content:center;font:500 32px var(--script);color:var(--pink)}

/* optin */
.optin{position:absolute;top:2890px;left:0;width:1200px;height:232px;background:linear-gradient(90deg,var(--orange),#f3955a)}
.cookies{position:absolute;left:1020px;top:0;width:180px;height:232px;background:linear-gradient(180deg,#b57a48,#d8a46c 50%,#c08a55);border-radius:90px 0 0 70px}
.optin h2{position:absolute;left:79px;top:40px;white-space:nowrap;font:500 40px var(--script);color:var(--white)}
.optin-field{position:absolute;top:127px;height:47px;border:2px solid rgba(255,255,255,.8);border-radius:24px;font:14px var(--sans);color:var(--white);padding:13px 26px}
.optin-submit{position:absolute;left:831px;top:127px;width:132px;height:47px;border-radius:24px;background:var(--white);font:700 22px var(--script);color:var(--pink);display:flex;align-items:center;justify-content:center}

/* footer */
.site-footer{position:absolute;top:3122px;left:0;width:1200px;height:295px;background:linear-gradient(180deg,var(--pink),var(--pink-deep))}
.footer-brand{position:absolute;left:79px;top:60px;display:flex;align-items:center;gap:10px;font:700 28px var(--script);color:var(--white);white-space:nowrap}
.footer-brand .brand-dot{background:var(--white);width:12px;height:12px}
.footer-tagline{position:absolute;left:79px;top:170px;width:240px;font:500 24px/30px var(--script);color:var(--white)}
.footer-col{position:absolute;top:60px;color:var(--white)}
.footer-col h4{font:500 24px var(--script);margin-bottom:16px}
.footer-col li{list-style:none;font:14px/42px var(--sans)}
.footer-col p{font:14px/22px var(--sans);width:200px}
.testimonial-name{margin-top:10px;font-weight:600}
.pager{display:flex;gap:12px;margin-top:34px}
.pager span{width:34px;height:34px;background:var(--white);display:flex;align-items:center;justify-content:center}
.contact li{display:flex;gap:14px;align-items:flex-start;line-height:22px;margin-bottom:16px}
.contact svg{flex:none;margin-top:2px}

.bottom-bar{position:absolute;top:3417px;left:0;width:1200px;height:65px;background:var(--orange);color:var(--white)}
.bottom-bar p{position:absolute;left:79px;top:23px;font:600 14px var(--sans)}
.social{position:absolute;left:830px;top:11px;display:flex;gap:14px}
.social span{width:42px;height:42px;border-radius:50%;border:2px solid var(--white)}
</style>
</head>
<body>

<svg width="0" height="0" style="position:absolute" aria-hidden="true">
  <defs>
    <pattern id="scallop-down" width="36" height="22" patternUnits="userSpaceOnUse">
      <path d="M0 0H36V10Q27 22 18 10Q9 -2 0 10Z" fill="#f3f1f0"/>
    </pattern>
    <pattern id="scallop-up" width="36" height="22" patternUnits="userSpaceOnUse">
      <path d="M0 22H36V12Q27 0 18 12Q9 24 0 12Z" fill="#f3f1f0"/>
    </pattern>
    <pattern id="scallop-down-white" width="36" height="22" patternUnits="userSpaceOnUse">
      <path d="M0 0H36V10Q27 22 18 10Q9 -2 0 10Z" fill="#ffffff"/>
    </pattern>
  </defs>
</svg>

<section class="hero">
  <div class="hero-photo" role="img" aria-label="Photo of Rosalind smiling and holding a plate of cake"></div>
  <div class="cake-plate" role="img" aria-label="Photo of a chocolate cake on a white plate"></div>
  <p class="hero-tagline">Gluten-free &amp; dairy-free sweets that are easy and delicious.</p>
  <svg class="hero-arrow" width="70" height="70" viewBox="0 0 70 70" aria-hidden="true">
    <path d="M58 4Q60 50 8 58" fill="none" stroke="#fff" stroke-width="2"/>
    <path d="M18 50L8 58L19 65" fill="none" stroke="#fff" stroke-width="2"/>
  </svg>
  <p class="hero-sign">Rosalind Marwell</p>
  <svg class="wave" style="top:651px" aria-hidden="true"><rect width="1200" height="22" fill="url(#scallop-up)"/></svg>
</section>

<header class="site-header">
  <nav class="main-nav">
    <span class="current">Home</span><span>/</span>
    <span>About</span><span>/</span>
    <span>Recipes</span><span>/</span>
    <span>Resources</span>
  </nav>
  <div class="search">Search Here...<span class="search-btn"></span></div>
  <svg class="wave" style="top:70px" aria-hidden="true"><rect width="1200" height="22" fill="url(#scallop-down-white)"/></svg>
</header>
<div class="brand"><span class="brand-dot"></span><span class="brand-name">The Honeyed Days</span></div>

<section class="newsletter">
  <h2>Newsletter Subscription</h2>
  <p>Subscribe to our Newsletter and get Latest Recipes. Join Our amazing Community to know much more.</p>
  <div class="nl-input">E-mail</div>
  <div class="btn btn-pink" style="left:740px;top:183px;width:146px;height:52px;font-size:15px">Subscribe</div>
</section>

<section class="welcome">
  <svg class="wave" style="top:0" aria-hidden="true"><rect width="1200" height="22" fill="url(#scallop-down)"/></svg>
  <h2>Welcome To The Honeyed Days</h2>
  <p>Lorem Ipsum is simply dummy text of the printing and typesetting industry. Lorem Ipsum has been the industry's standard dummy text ever since the 1500s, when an unknown printer took a galley of type and scrambled it to make a type specimen book. It has survived not only five centuries, but also the leap into...</p>
  <div class="btn btn-light" style="left:79px;top:237px;width:174px;height:51px">Read More &raquo;</div>
  <div class="icecream" role="img" aria-label="Photo of a scoop of vanilla ice cream with a wafer"></div>
</section>

<div class="family-photo" role="img" aria-label="Photo of Rosalind on a sofa hugging her two small children"></div>

<section class="about">
  <h2>About</h2>
  <p>Welcome to BeetBuddies. My name is Rosalind and my husband's name is Gideon. We have two kale cuties: Clara and Milo. Between my husband and I we have 7 allergies/sensitivities: gluten, dairy, egg, almond, cranberries, sesame seeds and coffee. If you think this list sounds overwhelming than you know...</p>
  <div class="btn btn-light" style="left:512px;top:214px;width:176px;height:50px">Read More &raquo;</div>
</section>

<section class="recipes">
  <svg class="wave" style="top:0" aria-hidden="true"><rect width="1200" height="22" fill="url(#scallop-down)"/></svg>
  <h2>Our Recipes</h2>
  <article class="recipe-card" style="left:77px">
    <div class="recipe-img" role="img" aria-label="Photo of a stack of oatmeal cookies" style="background:linear-gradient(180deg,#d9d4cc,#a9763e 40%,#8a5a2c)"></div>
    <h3>Breakfast</h3>
  </article>
  <article class="recipe-card" style="left:348px">
    <div class="recipe-img" role="img" aria-label="Photo of a creamy dip surrounded by sliced peppers and carrots" style="background:radial-gradient(circle at 50% 45%,#e6e2c8 0 30%,#e8863a 31%,#d8452a 70%,#f0a030)"></div>
    <h3>Lunch</h3>
  </article>
  <article class="recipe-card" style="left:617px">
    <div class="recipe-img" role="img" aria-label="Photo of sliced banana bread" style="background:linear-gradient(180deg,#8a5a3a,#c4875a 50%,#a86e48)"></div>
    <h3>Snack</h3>
  </article>
  <article class="recipe-card" style="left:889px">
    <div class="recipe-img" role="img" aria-label="Photo of a plate with ham, green beans and tomatoes" style="background:radial-gradient(circle at 50% 55%,#d89a8a 0 30%,#6a7a4a 50%,#5a6a72 80%)"></div>
    <h3>Dinner</h3>
  </article>
  <div class="btn btn-pink" style="left:522px;top:483px;width:156px;height:52px">View All &raquo;</div>
</section>

<section class="optin">
  <div class="cookies" role="img" aria-label="Photo of a stack of chocolate chip cookies"></div>
  <h2>Gluten-free &amp; dairy-free sweets that actually taste good</h2>
  <div class="optin-field" style="left:237px;width:278px">Enter Name</div>
  <div class="optin-field" style="left:529px;width:279px">Enter Email ID</div>
  <div class="optin-submit">Subscribe</div>
</section>

<footer class="site-footer">
  <svg class="abs" style="top:-30px;left:0" width="1200" height="44" viewBox="0 0 1200 44" aria-hidden="true">
    <path d="M0 30Q60 6 140 24T300 18Q360 4 440 26T600 22Q680 0 760 24T920 20Q990 6 1060 26T1200 18V44H0Z" fill="#e2456f"/>
  </svg>
  <div class="footer-brand"><span class="brand-dot"></span>The Honeyed Days</div>
  <p class="footer-tagline">Gluten-free &amp; dairy-free sweets that actually taste good</p>

  <div class="footer-col" style="left:350px">
    <h4>Useful Links</h4>
    <ul><li>Home</li><li>About</li><li>Recipes</li><li>Resources</li></ul>
  </div>

  <div class="footer-col" style="left:590px">
    <h4>Client Testimonial</h4>
    <p>Lorem Ipsum is simply dummy text of the printing and typesetting industry...</p>
    <p class="testimonial-name">&ndash; Client Name</p>
    <div class="pager">
      <span><svg width="12" height="14" viewBox="0 0 12 14"><path d="M9 1L3 7L9 13" fill="none" stroke="#e2456f" stroke-width="2"/></svg></span>
      <span><svg width="12" height="14" viewBox="0 0 12 14"><path d="M3 1L9 7L3 13" fill="none" stroke="#e2456f" stroke-width="2"/></svg></span>
    </div>
  </div>

  <div class="footer-col contact" style="left:870px">
    <h4>Get In Touch With Us</h4>
    <ul>
      <li><svg width="16" height="20" viewBox="0 0 16 20"><path d="M8 0C3.6 0 0 3.4 0 7.8 0 13 8 20 8 20S16 13 16 7.8C16 3.4 12.4 0 8 0Z" fill="#fff"/><circle cx="8" cy="7.8" r="3" fill="#e2456f"/></svg><span style="width:220px">123 Building name, Street Name, Area Name, Country.</span></li>
      <li><svg width="18" height="18" viewBox="0 0 18 18"><path d="M4 1L7 5L5 7Q7 11 11 13L13 11L17 14L15 17Q8 17 3 11Q0 6 1 3Z" fill="#fff"/></svg><span style="font-weight:600">123 456 7890</span></li>
      <li><svg width="18" height="14" viewBox="0 0 18 14"><rect width="18" height="14" rx="2" fill="#fff"/><path d="M1 1L9 8L17 1" fill="none" stroke="#e2456f" stroke-width="1.5"/></svg><span>info@thehoneyeddays.com</span></li>
      <li><svg width="18" height="18" viewBox="0 0 18 18"><circle cx="9" cy="9" r="8" fill="none" stroke="#fff" stroke-width="2"/><path d="M1 9H17M9 1Q4 9 9 17Q14 9 9 1" fill="none" stroke="#fff" stroke-width="1.5"/></svg><span>www.thehoneyeddays.com</span></li>
    </ul>
  </div>
</footer>

<div class="bottom-bar">
  <p>&copy; The Honeyed Days - 2017. All Rights Reserved.</p>
  <div class="social" aria-label="Social links">
    <span></span><span></span><span></span><span></span><span></span><span></span>
  </div>
</div>

</body>
</html>
```